Web Design Project

This design template will be for an HVAC contractor. The visitors of the site will be home owners who need a new heating/cooling system or who have a broken system and want service immediately.

We need to establish trust with the design and content. Homeowners want a dependable, professional, local, and responsive contractor to invite to their home to fix their problem.

Layout, color scheme, design, functionality, everything that has to the design is entirely up to you.

Use your creative abilities to generate a stunning design that will wow everyone that sees the site. The visitor should think “Wow, this company looks very professional for a local company, they offer what I need, and they have an impressive website- I’ll call them now”. We already have generic templates, give us something fresh.

Important: The images that are used in the design need to be from pixmarrow or another credible site like it. For this design do not worry if the “pixmarrow” is over it. If you think it should be included and it looks good with the design of the sites we will get the license to it. Product photos can be used from www.Volvex.example
Updates

Target Market(s)

Home owners who are looking for new heating and cooling equipment or immediate HVAC service

Industry/Entity Type

Contractor

Requirements
Must have
• Things that must be included.
Navigation Structure: Home, Services, Tour, Savings Calculator, About us, contact

Home Page:
Somewhere in the Header:
Room for two logo pictures (one of which will be Volvex’s logo)
Phone number (as an image)

Body:
Savings calculator form: Two text input boxes one for street address and zip code. A button below that showing “Savings Calculator”.

A vertically oriented form; parts to include on form: Name, Email, Phone Number, Service wanted, small comment box, check box with a Please contact me (default value is that the checkbox is checked.) Example: http://www.korlinair.example/

An area showing the areas served, this should list atleast 5 towns and adapt for more.
Images or buttons showing areas of focus: Heating, Cooling, Services, Maintenance (each with learn more links close to them) Example http://www.korlinair.example/

Areas for a paragraph or two of content: For now write whatever you think it should say.

Footer:
Text links to: Services (Heating, Cooling, Other Services, Maintenance), Savings (Savings Calculator, Home Tour, Energy savings), More Info (About, Contact us)
Certifications (Picture links)
Phone Number, address, contractor name as text and copy right info.

Content Page:
Same header and footer as the home page.
Request more information form (the same form that was on the home page)
Savings calculator entrance. Same fields as on home page.
Phone number (as image)
here is an example http://www.korlinair.example/

Contact Us Page:
Savings calculator
Phone number (as image)
Contact Form (Name: first and last, Email, Phone Number, Reason for contact, Large comments box, send information button) example

```html
<!DOCTYPE html>
<html lang="en">
<head>
<meta charset="utf-8">
<title>Corvalen HVAC</title>
<link rel="stylesheet" href="https://fonts.googleapis.com/css2?family=Yanone+Kaffeesatz:wght@400;500&family=Signika:wght@400;500&family=Arimo:wght@400;700&display=swap">
<style>
:root{
  --blue:#0a77c0;
  --blue-dark:#0868a8;
  --red:#e8200f;
  --red-dark:#c41405;
  --ink:#1c1c1c;
  --text:#555;
  --panel:#e4e4e4;
  --panel-soft:#efefef;
  --field:#d3d3d3;
  --field-line:#b9b9b9;
  --orange:#ff7f00;
  --yellow:#e5e03c;
  --sky:#63b5e3;
  --footer:#666;
  --footer-head:#bdbdbd;
  --footer-link:#e2e2e2;
}
*{box-sizing:border-box;margin:0;padding:0}
html,body{width:1053px;height:1200px;overflow:hidden;background:#fff}
.page{position:relative;width:1200px;height:1368px;transform:scale(.8775);transform-origin:0 0;font-family:Arimo,Arial,sans-serif;color:var(--text)}
.abs{position:absolute}
.condensed{font-family:"Yanone Kaffeesatz",sans-serif}

/* header */
.brand{left:90px;top:37px;display:flex;align-items:center;gap:10px;white-space:nowrap}
.brand-dot{width:44px;height:44px;border-radius:50%;background:var(--blue);flex:none}
.brand-name{font-family:Arimo,Arial,sans-serif;font-weight:700;font-size:17px;letter-spacing:4px;color:var(--ink)}
.partner{left:366px;top:47px;font-family:Arimo,Arial,sans-serif;font-weight:700;font-size:19px;color:var(--ink);white-space:nowrap}
.phone{right:87px;top:12px;font-size:33px;color:var(--ink);white-space:nowrap}
.nav{left:452px;top:59px;width:661px;height:38px}
.nav a{position:absolute;top:0;height:38px;line-height:42px;font-size:19px;color:var(--ink);text-decoration:none;font-family:"Yanone Kaffeesatz",sans-serif;white-space:nowrap}
.nav a.active{background:var(--blue);color:#fff;width:66px;text-align:center;left:0}

/* hero */
.hero{left:2px;top:97px;width:1198px;height:381px;background:radial-gradient(ellipse at 50% 40%,#1584cc,var(--blue-dark))}
.hero-photo{left:106px;top:135px;width:602px;height:305px;background:linear-gradient(120deg,#f3f3f3,#d9d9d9 55%,#c4c4c4)}
.slide-arrow{width:34px;height:34px;border-radius:50%;background:#2b2b2b;top:265px}
.hero-title{left:758px;top:140px;font-family:Signika,sans-serif;font-weight:500;font-size:31px;line-height:36px;color:#fff;white-space:nowrap}
.field{background:#fff;border:1px solid #cfcfcf;font-size:11px;color:#666;padding:8px 9px}
.calc-btn{left:756px;top:400px;width:215px;height:37px;border-radius:3px;background:linear-gradient(#fafafa,#d8d8d8);font-family:Signika,sans-serif;font-size:22px;color:var(--ink);text-align:center;line-height:37px;white-space:nowrap}

/* request form */
.request{left:85px;top:505px;width:271px;height:584px;background:var(--panel)}
.request-head{height:43px;background:linear-gradient(#f53a1c,var(--red-dark));color:#fff;font-size:27px;padding:8px 0 0 26px;font-family:"Yanone Kaffeesatz",sans-serif}
.label{font-size:13px;color:#444;white-space:nowrap}
.input{width:226px;height:30px;background:var(--field);border:1px solid var(--field-line)}
.pill{height:25px;border-radius:13px;background:linear-gradient(#ff4a25,var(--red-dark));color:#fff;font-weight:700;font-size:11px;display:flex;align-items:center;padding-left:8px;gap:10px;white-space:nowrap}
.pill i{width:14px;height:14px;border-radius:50%;background:#fff;display:flex;align-items:center;justify-content:center}

/* focus cards */
.card{top:506px;width:203px;height:223px;padding:15px 16px 17px}
.card-inner{background:#fff;border-radius:12px;height:100%;position:relative}
.card-title{position:absolute;left:18px;top:12px;font-size:26px;color:var(--ink);font-family:"Yanone Kaffeesatz",sans-serif}
.card-art{position:absolute;left:34px;top:48px;width:102px;height:132px;border-radius:14px}

/* content */
.article-title{left:392px;top:754px;font-size:25px;color:var(--ink);font-family:"Yanone Kaffeesatz",sans-serif;font-weight:500;white-space:nowrap}
.copy{font-size:13px;line-height:24px;text-align:justify}
.areas{left:378px;top:946px;width:731px;height:142px;background:var(--panel-soft);border-radius:3px}
.areas h2{font-family:Signika,sans-serif;font-weight:400;font-size:18px;color:var(--ink);position:absolute;left:15px;top:9px;white-space:nowrap}

/* footer */
.footer{left:0;top:1132px;width:1200px;height:236px;background:var(--footer)}
.foot-col{top:1155px}
.foot-col h3{font-family:"Yanone Kaffeesatz",sans-serif;font-weight:400;font-size:26px;color:var(--footer-head);margin-bottom:9px}
.foot-col li{list-style:none;font-size:14px;line-height:24px;color:var(--footer-link)}
.legal{right:88px;top:1304px;font-size:12px;color:var(--footer-link);white-space:nowrap}
</style>
</head>
<body>
<div class="page">

  <header>
    <div class="abs brand"><span class="brand-dot"></span><span class="brand-name">CORVALEN HVAC</span></div>
    <div class="abs partner">Volvex</div>
    <div class="abs phone condensed">CALL (555) 014 6789</div>
    <nav class="abs nav">
      <a class="active" href="#">HOME</a>
      <a href="#" style="left:112px">SERVICES</a>
      <a href="#" style="left:224px">TOUR</a>
      <a href="#" style="left:316px">SAVINGS CALCULATOR</a>
      <a href="#" style="left:498px">ABOUT US</a>
      <a href="#" style="left:612px">CONTACT</a>
    </nav>
  </header>

  <section class="abs hero"></section>
  <div class="abs hero-photo" role="img" aria-label="Technician servicing a wall-mounted air conditioning unit"></div>
  <svg class="abs slide-arrow" style="left:89px" viewBox="0 0 34 34"><path d="M20 10l-7 7 7 7" fill="none" stroke="#ccc" stroke-width="3"/></svg>
  <svg class="abs slide-arrow" style="left:691px" viewBox="0 0 34 34"><path d="M14 10l7 7-7 7" fill="none" stroke="#ccc" stroke-width="3"/></svg>
  <h1 class="abs hero-title">AIR CONDITIONING &amp;<br>FURNACE REPAIR &amp;<br>INSTALLATION</h1>
  <div class="abs field" style="left:757px;top:261px;width:236px;height:88px">Street Address</div>
  <div class="abs field" style="left:757px;top:357px;width:236px;height:28px;padding-top:7px">Zip Code</div>
  <div class="abs calc-btn">Calculate My Savings</div>

  <aside class="abs request">
    <div class="request-head">REQUEST INFORMATION</div>
    <div class="abs label" style="left:22px;top:58px">Name</div>
    <div class="abs input" style="left:22px;top:78px"></div>
    <div class="abs label" style="left:22px;top:127px">Email</div>
    <div class="abs input" style="left:22px;top:147px"></div>
    <div class="abs label" style="left:22px;top:196px">Phone</div>
    <div class="abs input" style="left:22px;top:216px"></div>
    <div class="abs label" style="left:22px;top:272px">Services</div>
    <div class="abs input" style="left:22px;top:296px"></div>
    <div class="abs label" style="left:22px;top:348px">Comments</div>
    <div class="abs input" style="left:22px;top:373px;height:82px"></div>
    <svg class="abs" style="left:23px;top:479px" width="13" height="13" viewBox="0 0 13 13"><rect x=".5" y=".5" width="12" height="12" fill="#fff" stroke="#777"/><path d="M3 6.5l2.5 2.5L10 3.5" fill="none" stroke="#2a4f9c" stroke-width="1.6"/></svg>
    <div class="abs label" style="left:42px;top:478px">Please Contact Me</div>
    <div class="abs pill" style="left:18px;top:544px;width:108px"><i><svg width="6" height="7" viewBox="0 0 6 7"><path d="M0 0l6 3.5L0 7z" fill="#e8200f"/></svg></i>SUBMIT</div>
  </aside>

  <div class="abs card" style="left:393px;background:var(--orange)"><div class="card-inner"><span class="card-title">HEATING</span><div class="card-art" role="img" aria-label="Furnace with flame icon" style="background:linear-gradient(#d7d7d7,#9b9b9b)"></div></div></div>
  <div class="abs card" style="left:647px;background:var(--yellow)"><div class="card-inner"><span class="card-title">COOLING</span><div class="card-art" role="img" aria-label="Outdoor condenser unit icon" style="background:linear-gradient(#4eaa3c,#2b7a25)"></div></div></div>
  <div class="abs card" style="left:904px;background:var(--sky)"><div class="card-inner"><span class="card-title">SERVICES</span><div class="card-art" role="img" aria-label="Wrench and screwdriver icon" style="background:linear-gradient(#5fb4f0,#f4b400)"></div></div></div>

  <h2 class="abs article-title">AIR CONDITIONER REPAIR: WATER LEAK AT INDOOR UNIT - THE CAUSES AND SOLUTIONS</h2>
  <p class="abs copy" style="left:392px;top:798px;width:715px">Lorem Ipsum is simply dummy text of the printing and typesetting industry. Lorem Ipsum has been the industry's standard dummy text ever since the 1500s, when an unknown printer took a galley of type and scrambled it to make a type specimen book. It has survived not only five centuries, but also the leap into electronic typesetting, remaining essentially unchanged. It was popularised in the 1960s with the release of Transfera sheets containing Lorem Ipsum passages, and more recently with desktop publishing software like Pagewright including versions of Lorem Ipsum.</p>
  <div class="abs pill" style="left:1005px;top:909px;width:104px;gap:8px"><i><svg width="6" height="7" viewBox="0 0 6 7"><path d="M0 0l6 3.5L0 7z" fill="#e8200f"/></svg></i>READ MORE</div>

  <section class="abs areas">
    <h2>AREAS SERVED / COMMUNITIES SERVED</h2>
    <p class="abs copy" style="left:9px;top:50px;width:715px">Lorem Ipsum is simply dummy text of the printing and typesetting industry. Lorem Ipsum has been the industry's standard dummy text ever since the 1500s, when an unknown printer took a galley of type and scrambled it to make a type specimen book. It has survived not only five centuries, but also the leap into electronic typesetting, remaining essentially unchanged.</p>
  </section>

  <footer class="abs footer"></footer>
  <div class="abs foot-col" style="left:90px"><h3>SERVICES</h3><ul><li>Subitem 1</li><li>Subitem 1</li><li>Subitem 1</li><li>Subitem 1</li><li>Subitem 1</li><li>Subitem 1</li></ul></div>
  <div class="abs foot-col" style="left:238px"><h3>SAVINGS</h3><ul><li>Subitem 1</li><li>Subitem 1</li><li>Subitem 1</li><li>Subitem 1</li><li>Subitem 1</li><li>Subitem 1</li></ul></div>
  <div class="abs foot-col" style="left:399px"><h3>ABOUT US</h3><ul><li>Subitem 1</li><li>Subitem 1</li><li>Subitem 1</li><li>Subitem 1</li><li>Subitem 1</li><li>Subitem 1</li></ul></div>
  <div class="abs foot-col" style="left:588px"><h3>TOUR</h3><ul><li>Subitem 1</li><li>Subitem 1</li><li>Subitem 1</li><li>Subitem 1</li><li>Subitem 1</li><li>Subitem 1</li></ul></div>
  <div class="abs legal">© &nbsp;2012. All Rights Reserved</div>

</div>
</body>
</html>
```